Yard Sign Manufacturing Company Needs a Website Design

We manufacture a variety of products including yard signs and would like to develop a stand alone website to cater to this business unit.

Competitor sites:
https://www.plotmarker.com/yard-signs/
http://www.boardly.com/

A few things to keep in mind/ elements we like from the competitors sites:
1) We do offer design services if someone dones not have a design

2) We would like the user to have the option to either select a template (based on industry: political, real estate, etc) or upload their own file

3) the site will focus on yard signs exclusively

4) Pricing, turn times, and ease of use seem to be the biggest factors in selecting a manufacturer

5) User experience/ flow is very important to us. We would like someone to be able to move forward with their sign selection/creation within the first click.

I like the "post a project" feel of pitchhive.
Also, quickplate.com does a nice job of making it easy for the user to complete project with just a few clicks.

Pages I would like designed are the #1) homepage (prefer user to select whether to upload their own design or a template) #2) design page/upload page #3) checkout page

Target Market(s)

consumers of yard signs

Industry/Entity Type

Business

Number of Pages Required

3 page

Colors
0455a3
33a6d7
d0dfed

Requirements
Must have
• Element for user to upload their own design
• Element for users select a template -preferably sorted by industry
• Element for user to modify selected template for example - (https://www.lawnplacards.com/EditTool.aspx?T=9A1B2C3D4E5F60718293A4B5C6D7E8F90A1B2C3D4E5F6071&S=2&M=1&CID=8027)
Nice to have
• minimal clicks to move forward with sign project

```html
<!DOCTYPE html>
<html lang="en">
<head>
<meta charset="utf-8">
<title>Yard Signs – Home</title>
<link rel="stylesheet" href="https://fonts.googleapis.com/css2?family=Lato:wght@400;700;900&family=Varela+Round&display=swap">
<style>
:root{
  --brand-dark:#0455a3;
  --brand:#33a6d7;
  --brand-pale:#d0dfed;
  --side:#2d9fd6;
  --page:#ededed;
  --ink:#333;
  --muted:#666;
  --footer:#2f2f2f;
  --footer-deep:#1f1f1f;
  --footer-text:#bdbdbd;
  --line:#c9c9c9;
}
*{box-sizing:border-box;margin:0;padding:0}
html,body{width:952px;height:1200px;overflow:hidden}
body{position:relative;background:var(--page);font-family:"Lato",Arial,sans-serif;color:var(--ink)}
.abs{position:absolute}

.topbar{left:0;top:0;width:952px;height:35px;background:linear-gradient(#f7f7f7,#e2e2e2);border-bottom:1px solid #cfcfcf}
.topbar-links{left:140px;top:10px;font-size:11px;display:flex;gap:9px;color:#333}
.cart{left:607px;top:10px;font-size:11px;display:flex;align-items:center;gap:8px}
.btn-small{top:8px;height:18px;font-size:10px;font-weight:700;border:1px solid #bbb;border-radius:3px;background:linear-gradient(#fff,#e8e8e8);display:flex;align-items:center;justify-content:center}
.register{left:692px;width:51px}
.login{left:749px;width:53px}

.logo{left:156px;top:48px;font-size:24px;font-weight:700;color:var(--brand-dark);display:flex;align-items:center;gap:6px}
.logo-dot{width:10px;height:10px;background:var(--brand)}
.search{left:613px;top:56px;width:181px;height:16px;border:1px solid #ccc;background:#fff;font-size:9px;color:#aaa;padding:2px 5px}
.search-btn{left:794px;top:56px;width:17px;height:16px;background:var(--brand-dark);display:flex;align-items:center;justify-content:center}

.mainnav{left:136px;top:90px;width:680px;height:24px;background:var(--brand);display:flex;justify-content:center;align-items:center}
.mainnav a{color:#fff;font-size:9.5px;letter-spacing:.4px;text-decoration:none;padding:0 11px;border-left:1px solid rgba(255,255,255,.35);line-height:24px}
.mainnav a:first-child{border-left:none}

.side-title{left:147px;top:123px;font-size:13px;font-weight:700;color:#333}
.side-list{left:148px;top:156px;width:144px;background:var(--side);list-style:none;padding:2px 0 3px}
.side-list li{height:21.2px;margin:0 4px;border-bottom:1px solid rgba(255,255,255,.35);color:#fff;font-size:9.5px;display:flex;justify-content:space-between;align-items:center;padding:0 6px}
.side-list li::after{content:"›";font-size:12px}

.hero{left:311px;top:124px;width:491px;height:261px;background:linear-gradient(180deg,#b9c6cf 0%,#8ea08c 45%,#5f7f3f 70%,#4f6f2f 100%)}
.why{left:585px;top:197px;width:185px;height:159px;background:rgba(4,85,163,.88);color:#fff;padding:10px 6px}
.why h2{font-family:"Varela Round",sans-serif;font-weight:400;font-size:13px;padding-bottom:8px;border-bottom:1px solid rgba(255,255,255,.7);margin-bottom:10px}
.why ul{list-style:none;padding-left:8px}
.why li{font-size:10px;display:flex;align-items:center;gap:7px;height:22px}
.tick{width:11px;height:11px;background:#fff;display:flex;align-items:center;justify-content:center}

.config{left:328px;top:408px;font-size:10px;color:#555;display:flex;align-items:center;gap:6px}
.field{border:1px solid #bbb;background:#f6f6f6;height:16px;font-size:9px;padding:0 5px;display:flex;align-items:center}
.price{color:var(--brand-dark)}
.btn-primary{background:var(--brand-dark);color:#fff;border-radius:3px;display:flex;align-items:center;justify-content:center;font-family:"Varela Round",sans-serif}
.start-small{left:702px;top:438px;width:100px;height:23px;font-size:11px}

.section-head{left:311px;top:477px;width:491px;height:24px;display:flex;align-items:center;gap:10px}
.section-head .rule{flex:1;height:1px;background:#aaa}
.section-head h2{font-family:"Varela Round",sans-serif;font-weight:400;font-size:19px;color:#333}
.chev{width:20px;height:20px;border-radius:50%;background:#bbb;display:flex;align-items:center;justify-content:center}

.card{width:141px;height:160px;background:#fff;border:1px solid #ddd;box-shadow:0 1px 3px rgba(0,0,0,.2);padding:5px}
.card-img{width:129px;height:121px}
.card-foot{display:flex;height:30px;margin-top:2px}
.card-name{flex:1;font-size:9px;color:#666;line-height:11px;padding:4px 0 0 6px;border-right:1px solid #ddd}
.card-count{width:54px;font-size:15px;font-weight:700;color:#333;display:flex;align-items:center;justify-content:center}

.start-big{left:460px;top:894px;width:206px;height:32px;font-size:16px;justify-content:flex-start;padding-left:16px}
.start-big .arrow{position:absolute;right:0;top:0;width:44px;height:32px;border-left:1px solid rgba(255,255,255,.3);display:flex;align-items:center;justify-content:center}

.footer{left:0;top:945px;width:952px;height:221px;background:var(--footer)}
.footer-col h3{font-size:12px;font-weight:700;color:#fff;letter-spacing:-.2px;margin-bottom:10px}
.footer-col ul{list-style:none;width:100px}
.footer-col li{font-size:8px;color:var(--footer-text);height:18px;line-height:15px;border-bottom:1px solid #3d3d3d}
.input{background:#262626;border:1px solid #474747;border-radius:2px;font-size:9px;color:#888;padding:3px 6px}
.submit{left:594px;top:1111px;width:53px;height:21px;background:var(--brand-dark);color:#fff;font-size:10px;font-weight:700;border-radius:2px;display:flex;align-items:center;justify-content:center}
.divider{left:664px;top:958px;width:1px;height:195px;background:#444}
.news{left:681px;top:961px;font-size:9px;color:#fff;font-weight:700;display:flex;align-items:center;gap:7px}
.news-box{left:680px;top:984px;width:145px;height:22px;border:2px solid #fff;border-radius:2px;background:#262626;font-size:9px;color:#888;padding:3px 6px}
.join{left:790px;top:987px;width:32px;height:16px;background:var(--brand-dark);color:#fff;font-size:9px;display:flex;align-items:center;justify-content:center}
.social{left:681px;top:1027px;display:flex;gap:10px;font-size:9px;color:#fff;font-weight:700}
.social span,.pay span{display:flex;align-items:center;gap:3px}
.social i{width:8px;height:8px;border-radius:50%;background:var(--brand);display:inline-block}
.pay{left:681px;top:1078px;display:flex;gap:14px;font-size:10px;font-weight:700;color:#ddd}
.foot-logo{left:707px;top:1133px;font-size:17px;font-weight:700;color:#888}
.bottombar{left:0;top:1166px;width:952px;height:34px;background:var(--footer-deep);font-size:8px;color:#888;display:flex;align-items:center;justify-content:center}
</style>
</head>
<body>

<header>
  <div class="abs topbar"></div>
  <nav class="abs topbar-links"><span>Categories</span><span>Designers</span><span>Price Quotes</span><span>How it works</span></nav>
  <div class="abs cart">
    <svg width="11" height="10" viewBox="0 0 11 10"><path d="M0 1h2l2 5h5l2-4H3" fill="none" stroke="#0455a3" stroke-width="1.4"/><circle cx="4.5" cy="8.5" r="1" fill="#0455a3"/><circle cx="8.5" cy="8.5" r="1" fill="#0455a3"/></svg>
    <span>Add to Cart</span>
  </div>
  <div class="abs btn-small register">Register</div>
  <div class="abs btn-small login">Log in</div>

  <div class="abs logo"><span class="logo-dot"></span>Yard Signs</div>
  <div class="abs search">Search here...</div>
  <div class="abs search-btn"><svg width="9" height="9" viewBox="0 0 9 9"><circle cx="3.7" cy="3.7" r="2.7" fill="none" stroke="#fff" stroke-width="1.3"/><path d="M5.7 5.7L8.5 8.5" stroke="#fff" stroke-width="1.4"/></svg></div>

  <nav class="abs mainnav">
    <a>HOME</a><a>BANNERS</a><a>YARD SIGNS</a><a>RIGID PLASTIC</a><a>POLITICAL SIGNS</a><a>REAL ESTATE SIGNS</a><a>MORE SIGNS</a>
  </nav>
</header>

<aside>
  <h2 class="abs side-title">Category</h2>
  <ul class="abs side-list">
    <li>Political Signs</li><li>Real Estate Signs</li><li>Contractor Signs</li><li>Aluminium Signs</li>
    <li>Yard Signs</li><li>Acrylic Signs</li><li>Wooden Sign</li><li>A-Frame Signs</li>
    <li>PVC Signs</li><li>Bandit Signs</li><li>Foam Boards</li><li>Wall Decals</li>
    <li>Clear Window Decals</li><li>Clear Car Decal</li><li>Opaque Car Decal</li><li>Opaque Static Cling</li>
    <li>Falconboard</li><li>Retractable Banner</li><li>Magnet</li><li>Backlit Decals</li>
    <li>Spider Stakes</li><li>Parking Signs</li><li>Heavy Wire Stakes</li><li>Other</li>
  </ul>
</aside>

<main>
  <div class="abs hero" role="img" aria-label="Photo of a real estate yard sign standing on a lawn in front of a house"></div>
  <section class="abs why">
    <h2>Why Choose Yard Signs</h2>
    <ul>
      <li><span class="tick"><svg width="8" height="8" viewBox="0 0 8 8"><path d="M1 4l2 2 4-5" fill="none" stroke="#0455a3" stroke-width="1.6"/></svg></span>Free Photos &amp; Signs</li>
      <li><span class="tick"><svg width="8" height="8" viewBox="0 0 8 8"><path d="M1 4l2 2 4-5" fill="none" stroke="#0455a3" stroke-width="1.6"/></svg></span>Free Shipping on Orders $50*</li>
      <li><span class="tick"><svg width="8" height="8" viewBox="0 0 8 8"><path d="M1 4l2 2 4-5" fill="none" stroke="#0455a3" stroke-width="1.6"/></svg></span>Order Today, Ship Tomorrow</li>
      <li><span class="tick"><svg width="8" height="8" viewBox="0 0 8 8"><path d="M1 4l2 2 4-5" fill="none" stroke="#0455a3" stroke-width="1.6"/></svg></span>Upload Your Own Design</li>
    </ul>
  </section>

  <div class="abs config">
    <span>Sign Type:</span><span class="field">Political Signs &nbsp;⌄</span>
    <span>Size(inches):</span><span class="field">W</span><span class="field">80</span><span class="field">H</span><span class="field">35</span>
    <span>Qty:</span><span class="field">2</span>
    <span>Price Each: <span class="price">$52.44</span></span>
  </div>
  <div class="abs btn-primary start-small">Get Started Now</div>

  <div class="abs section-head">
    <span class="rule"></span>
    <h2>Yard Signs Category</h2>
    <span class="chev"><svg width="9" height="6" viewBox="0 0 9 6"><path d="M1 1l3.5 3.5L8 1" fill="none" stroke="#fff" stroke-width="1.6"/></svg></span>
    <span class="rule"></span>
  </div>

  <article class="abs card" style="left:318px;top:524px">
    <div class="card-img" role="img" aria-label="Political campaign yard sign on grass" style="background:linear-gradient(#3b6a9a 0%,#2a6a2a 60%,#4a8a30 100%)"></div>
    <div class="card-foot"><div class="card-name">Political<br>Signs</div><div class="card-count">165</div></div>
  </article>
  <article class="abs card" style="left:492px;top:524px">
    <div class="card-img" role="img" aria-label="Retail space for lease sign on a lawn" style="background:linear-gradient(#8aa0b0 0%,#b83a30 45%,#6a8a40 100%)"></div>
    <div class="card-foot"><div class="card-name">Real Estate<br>Signs</div><div class="card-count">120</div></div>
  </article>
  <article class="abs card" style="left:666px;top:524px">
    <div class="card-img" role="img" aria-label="Brushed aluminium plaque on a stone wall" style="background:linear-gradient(135deg,#9a9a96,#6e6e6a)"></div>
    <div class="card-foot"><div class="card-name">Aluminium<br>Signs</div><div class="card-count">125</div></div>
  </article>
  <article class="abs card" style="left:318px;top:703px">
    <div class="card-img" role="img" aria-label="Red, white and blue yard sign on grass" style="background:linear-gradient(#c8d0d8 0%,#e8e8ee 40%,#4a7a30 100%)"></div>
    <div class="card-foot"><div class="card-name">Yard<br>Signs</div><div class="card-count">227</div></div>
  </article>
  <article class="abs card" style="left:492px;top:703px">
    <div class="card-img" role="img" aria-label="Parking signs on a pole against a blue sky" style="background:linear-gradient(#2f6fb8,#8ab0d8)"></div>
    <div class="card-foot"><div class="card-name">Parking<br>Signs</div><div class="card-count">232</div></div>
  </article>
  <article class="abs card" style="left:666px;top:703px">
    <div class="card-img" role="img" aria-label="Birdcage wall decals above a dining table" style="background:linear-gradient(#f2f2f2,#d8d4cc)"></div>
    <div class="card-foot"><div class="card-name">Wall<br>Decals</div><div class="card-count">140</div></div>
  </article>

  <div class="abs btn-primary start-big">Get Started Now
    <span class="arrow"><svg width="18" height="18" viewBox="0 0 18 18"><circle cx="9" cy="9" r="9" fill="#0a3f78"/><path d="M7.5 5l4 4-4 4" fill="none" stroke="#fff" stroke-width="2"/></svg></span>
  </div>
</main>

<footer>
  <div class="abs footer"></div>
  <div class="abs footer-col" style="left:129px;top:962px">
    <h3>I need a...</h3>
    <ul><li>Heavy Wire Stakes</li><li>Foam Boards</li><li>Bandit Signs</li><li>Brushed Aluminium</li><li>Rigid Plastic</li><li>Fabric Banners</li><li>Vinyl Lettering</li><li>All sign design services</li></ul>
  </div>
  <div class="abs footer-col" style="left:249px;top:962px">
    <h3>Find a...</h3>
    <ul><li>Parking Signs</li><li>Real Estate Signs</li><li>Frosted Decals</li><li>Falconboard</li><li>Flyer designer</li><li>Price Quotes</li><li>Wall Decals</li><li>See the full list</li></ul>
  </div>
  <div class="abs footer-col" style="left:367px;top:962px">
    <h3>About us</h3>
    <ul><li>About us</li><li>How it works</li><li>Contact Us</li><li>Affiliate Program</li><li>Submit Signs</li><li>Press</li><li>Help / FAQ</li><li>Blog</li></ul>
  </div>
  <div class="abs footer-col" style="left:492px;top:962px"><h3>Quick Contact</h3></div>
  <div class="abs input" style="left:492px;top:985px;width:155px;height:20px">Name...</div>
  <div class="abs input" style="left:492px;top:1013px;width:155px;height:21px">Email...</div>
  <div class="abs input" style="left:492px;top:1042px;width:155px;height:60px">Subject...</div>
  <div class="abs submit">Submit</div>

  <div class="abs divider"></div>
  <div class="abs news"><svg width="13" height="9" viewBox="0 0 13 9"><rect width="13" height="9" fill="#fff"/><path d="M0 0l6.5 5L13 0" fill="none" stroke="#2f2f2f" stroke-width="1.2"/></svg>Subscribe to our newsletter</div>
  <div class="abs news-box">Email...</div>
  <div class="abs join">Join</div>
  <div class="abs social"><span><i></i>Chirp</span><span><i></i>Plusr</span><span><i></i>Facio</span><span><i></i>Pinly</span></div>
  <div class="abs pay"><span>PayWell</span><span>Carda</span><span>Findcard</span></div>
  <div class="abs foot-logo">Yard Signs</div>

  <div class="abs bottombar">© Copyright information here</div>
</footer>

</body>
</html>
```